Dune Air & Plus business card

I need an awesome, double-sided business card designed with our new logo. I would like the one side black with the colored logo, and the back side is all yours. I'd like to see horizontal and vertical layouts. Get creative! Thank you.

Target Market(s)

HVAC, Heating and Cooling in Phoenix, AZ

Industry/Entity Type

HVAC

Contact Information for Business Card

We need our new logo on the card. Tom Harker, (623) 555-0142, tom@trydunesair.com, www.trydunesair.com, ROC 514273

```html
<!DOCTYPE html>
<html lang="en">
<head>
<meta charset="utf-8">
<title>Dune Air &amp; Plus — Business Card</title>
<link href="https://fonts.googleapis.com/css2?family=Montserrat:wght@400;500;700;800&display=swap" rel="stylesheet">
<style>
  :root {
    --backdrop: #2b2b2d;
    --card: #060606;
    --blue: #1a82dc;
    --blue-bright: #0f8ff0;
    --orange: #f07a24;
    --orange-deep: #e8542a;
    --white: #f4f4f4;
  }
  * { box-sizing: border-box; margin: 0; padding: 0; }
  html, body { width: 1200px; height: 900px; overflow: hidden; }
  body {
    background: var(--backdrop);
    font-family: "Montserrat", sans-serif;
    color: var(--white);
    display: flex;
    flex-direction: column;
    align-items: center;
    justify-content: center;
    gap: 36px;
  }
  .card {
    position: relative;
    width: 700px;
    height: 400px;
    background: var(--card);
    overflow: hidden;
    box-shadow: 0 10px 30px rgba(0,0,0,.55);
  }

  /* Front */
  .card-front .brand {
    position: absolute;
    inset: 0 0 14px 0;
    display: flex;
    align-items: center;
    justify-content: center;
    gap: 16px;
  }
  .brand-dot {
    width: 22px; height: 22px;
    border-radius: 50%;
    background: var(--orange);
  }
  .card-front .brand-name {
    font-weight: 800;
    font-size: 46px;
    color: var(--blue);
    letter-spacing: .5px;
  }
  .card-front .base-band {
    position: absolute;
    left: 0; right: 0; bottom: 0;
    height: 14px;
    background: var(--blue);
  }

  /* Back */
  .card-back .brand {
    position: absolute;
    left: 40px; top: 58px;
    display: flex;
    align-items: center;
    gap: 12px;
  }
  .card-back .brand-dot { width: 16px; height: 16px; }
  .card-back .brand-name {
    font-weight: 800;
    font-size: 30px;
    color: var(--blue);
  }
  .divider {
    position: absolute;
    left: 40px; right: 44px; top: 212px;
    height: 2px;
    background: var(--white);
  }
  .contact {
    position: absolute;
    left: 40px; top: 228px;
    list-style: none;
    display: flex;
    flex-direction: column;
    gap: 8px;
  }
  .contact li {
    display: flex;
    align-items: center;
    gap: 14px;
    font-size: 21px;
    font-weight: 400;
  }
  .contact svg { width: 18px; height: 18px; flex: none; }
  .person {
    position: absolute;
    right: 44px; top: 146px;
    text-align: right;
  }
  .person-name {
    font-weight: 800;
    font-size: 36px;
    color: var(--blue);
    letter-spacing: -.5px;
  }
  .person-role {
    font-size: 20px;
    font-weight: 500;
    color: var(--orange);
    letter-spacing: 1px;
  }
  .base-bands {
    position: absolute;
    left: 0; bottom: 0;
    width: 100%; height: 60px;
  }
  .licence {
    position: absolute;
    right: 110px; bottom: 12px;
    font-weight: 700;
    font-size: 22px;
    color: var(--white);
  }
</style>
</head>
<body>

<section class="card card-front" aria-label="Card front">
  <div class="brand">
    <span class="brand-dot"></span>
    <span class="brand-name">Dune Air &amp; Plus</span>
  </div>
  <div class="base-band"></div>
</section>

<section class="card card-back" aria-label="Card back">
  <div class="brand">
    <span class="brand-dot"></span>
    <span class="brand-name">Dune Air &amp; Plus</span>
  </div>

  <div class="person">
    <p class="person-name">TOM HARKER</p>
    <p class="person-role">Managing Director</p>
  </div>

  <div class="divider"></div>

  <ul class="contact">
    <li>
      <svg viewBox="0 0 24 24" aria-hidden="true"><path fill="#f07a24" d="M6.6 10.8a15.1 15.1 0 0 0 6.6 6.6l2.2-2.2a1 1 0 0 1 1-.25 11.4 11.4 0 0 0 3.6.57 1 1 0 0 1 1 1V20a1 1 0 0 1-1 1A17 17 0 0 1 3 4a1 1 0 0 1 1-1h3.5a1 1 0 0 1 1 1c0 1.25.2 2.45.57 3.57a1 1 0 0 1-.25 1z"/></svg>
      (623) 555-0142
    </li>
    <li>
      <svg viewBox="0 0 24 24" aria-hidden="true"><rect x="2" y="5" width="20" height="14" fill="#f07a24"/><path d="M2 5l10 8 10-8" fill="none" stroke="#060606" stroke-width="1.6"/></svg>
      tom@trydunesair.com
    </li>
    <li>
      <svg viewBox="0 0 24 24" aria-hidden="true"><circle cx="12" cy="12" r="10" fill="#f07a24"/><path d="M2 12h20M12 2c3 3 3 17 0 20M12 2c-3 3-3 17 0 20" fill="none" stroke="#060606" stroke-width="1.4"/></svg>
      www.trydunesair.com
    </li>
  </ul>

  <svg class="base-bands" viewBox="0 0 700 60" preserveAspectRatio="none" aria-hidden="true">
    <defs>
      <linearGradient id="orangeBand" x1="0" x2="1">
        <stop offset="0" stop-color="#e8542a"/>
        <stop offset="1" stop-color="#f79a20"/>
      </linearGradient>
    </defs>
    <polygon points="0,6 410,6 392,22 0,22" fill="url(#orangeBand)"/>
    <polygon points="0,26 380,26 420,0 700,0 700,60 0,60" fill="#1a82dc" transform="translate(0,0)"/>
    <polygon points="0,26 380,26 420,0 700,0 700,8 0,34" fill="#060606" opacity="0"/>
    <rect x="0" y="34" width="390" height="26" fill="#060606"/>
  </svg>
  <p class="licence">ROC 514273</p>
</section>

</body>
</html>
```